UI Design for a pre-ordering & Universal loyalty mobile app

We have built a central universal, preordering and gamification mobile app for alot of F&B merchant. The app is called PIXU (Pixoo as in eating something fast). Main goal for this app is too
1. Give users a universal loyalty system where they can accumulate loyalty points and use it on any brands
2. Gives user the ability to preorder for their food or drinks on the app and pick it up instore
3. There will be an E-wallet that is general or there can be a brand e-wallet (where they top-up with the brand only and get extra bonus)
4. There will be promotion such as games, top-up bonuses and rewards.
5. Community app where they can send money or promotion to their friends and will be able to play games together
This app is developed on the Flutter framework and also uses fontawesome font/icon package. Please consider this when doing the UI design for the app.
We are planning to create a mascot for our app as well and when it comes to color and icon, it's not set in stone and we are open for ideas.
I will attached our app icon and a few of our screens for your reference and each page details as follows:
Navigation bar.
There is a navigation bar on the top that should be visible on all screen. On the left will be a button to enter the menu which gives user more option and on the right will be a place for them to scan their QR code for loyalty points or payment and also a button to access their e-wallet.
1. Home screen
This screen is basically the main screen after user login. In this screen there will be
- Main banner (main promotions that's controlled by us)
- Specials banner (smaller) that will be controlled by the store/brands
- Favourite Store or Favourite food/drinks that user pre-configure
2. Shop screen (or can be called something else)
This screen is where they can browse all our participating stores. This screen will include
- Categories (filter)
- Brands which user can click and only view the brand page and stores
- All stores sorted by distances
3. Brand screen
The brand screen gives our brand with multiple store a presense on the app that is branded for them. They can have their own color scheme, logo and will only display their own store
4. Store screen
This will display all the store details, opening time, location, contact information etc.
- This screen will contain a banner/store image
- Store details
- Categories
- Food/drinks within the category
5. Order history screen
This will display their current order or their past order. Not sure if it should be on the main navigation or the sub navigation.
When making the UI design, please work on a color theme that will suit and also consider a mascot design in the future.
Feel free to ask me any questions before proceeding.
Thanks

```html
<!DOCTYPE html>
<html lang="en">
<head>
<meta charset="utf-8">
<title>PIXU – Mobile App Screens</title>
<link href="https://fonts.googleapis.com/css2?family=Barlow:wght@400;500;600&family=Barlow+Semi+Condensed:wght@500;600&display=swap" rel="stylesheet">
<style>
:root{
  --canvas:#e1e1e1;
  --phone:#ffffff;
  --bar:#f1f1f1;
  --ink:#1f1f1f;
  --muted:#555;
  --green:#7bd13b;
  --green-soft:#f1fbe6;
  --blue:#55aee8;
  --star:#f5c400;
  --line:#e4e4e4;
  --mascot:#f7c531;
}
*{box-sizing:border-box;margin:0;padding:0}
html,body{width:1200px;height:776px;overflow:hidden}
body{background:var(--canvas);font-family:"Barlow",sans-serif;color:var(--ink);position:relative}
.phone{position:absolute;width:265px;height:584px;background:var(--phone);border-radius:20px;overflow:hidden;box-shadow:0 6px 24px rgba(0,0,0,.06)}
.phone--home{left:95px;top:57px}
.phone--shop{left:468px;top:135px}
.phone--orders{left:841px;top:57px}
.abs{position:absolute}
.status{left:14px;top:8px;font-size:10px;font-weight:500}
.status-icons{right:18px;top:11px;display:flex;gap:3px}
.appbar{left:0;top:28px;width:100%;height:44px;background:var(--bar)}
.appbar .menu{left:16px;top:15px}
.appbar .title{left:42px;top:15px;font-family:"Barlow Semi Condensed",sans-serif;font-weight:500;font-size:11px;letter-spacing:.3px}
.brandmark{left:118px;top:6px;width:30px;text-align:center}
.brandmark .dot{width:24px;height:24px;border-radius:50%;background:var(--mascot);margin:0 auto}
.brandmark .name{font-size:5px;font-weight:600;margin-top:1px}
.appbar .qr{left:207px;top:14px}
.appbar .wallet{left:234px;top:14px}
.h2{font-family:"Barlow Semi Condensed",sans-serif;font-weight:600;font-size:14px;letter-spacing:.2px}
.hero{left:14px;top:85px;width:237px;height:150px;border-radius:4px;background:radial-gradient(ellipse at 50% 50%,#c59a7d 0%,#e9dcd4 45%,#fff 72%)}
.hero-title{left:0;width:100%;top:241px;text-align:center;font-family:"Barlow Semi Condensed",sans-serif;font-weight:600;font-size:14px}
.hero-sub{left:0;width:100%;top:260px;text-align:center;color:var(--green);font-size:9px;letter-spacing:6px;font-weight:600;padding-left:6px}
.deal{top:321px;height:96px;border-radius:2px}
.deal--a{left:20px;width:191px;background:linear-gradient(90deg,#a9d42a 0%,#d8e63a 45%,#e52521 60%,#d61f1c 100%)}
.deal--b{left:225px;width:60px;background:linear-gradient(90deg,#7a1414,#c6262a)}
.card{border-radius:26px;background:#f2f2f2;height:51px;width:222px;left:20px}
.thumb{position:absolute;left:5px;top:5px;width:41px;height:41px;border-radius:50%;background:radial-gradient(circle at 45% 40%,#b9916a,#5b3a24)}
.card .name{position:absolute;left:57px;top:12px;font-size:10.5px;font-weight:600}
.card .addr{position:absolute;left:57px;top:27px;font-size:10px;color:var(--muted);display:flex;align-items:center;gap:2px;white-space:nowrap}
.fav{position:absolute;width:26px;height:26px;border-radius:50%;background:var(--blue);display:flex;align-items:center;justify-content:center;right:-8px;top:-10px;border:2px solid #fff}
.search{left:16px;top:84px;width:232px;height:30px;border:1px solid #bdbdbd;border-radius:16px;font-size:10px;color:#555;padding:8px 15px}
.search svg{position:absolute;right:14px;top:9px}
.cat{top:154px;width:50px;height:56px;background:#fff;border-radius:3px;box-shadow:0 1px 4px rgba(0,0,0,.08);text-align:center;font-size:7px;padding-top:8px;line-height:1.2}
.cat svg{display:block;margin:0 auto 3px}
.cat.active{border-bottom:3px solid var(--green)}
.brand{top:265px;width:34px;height:34px;border-radius:2px}
.navbar{left:0;bottom:0;width:100%;height:52px;background:#fff}
.navdot{position:absolute;width:7px;height:7px;border-radius:50%;background:var(--green);left:31px;top:3px}
.navicon{position:absolute;top:16px}
.order{left:19px;width:226px;height:95px;border:1px solid var(--line);border-radius:2px;overflow:hidden;background:#fff}
.order .top{position:absolute;left:0;top:0;width:100%;height:60px;background:var(--green-soft)}
.order .thumb{left:11px;top:8px;width:30px;height:30px}
.order .name{position:absolute;left:59px;top:9px;font-size:10px;font-weight:600}
.order .addr{position:absolute;left:59px;top:25px;font-size:10px;color:var(--muted);line-height:1.2}
.badge{position:absolute;right:12px;top:7px;background:var(--blue);color:#fff;font-size:7.5px;font-weight:600;padding:4px 7px;border-radius:2px}
.viewmenu{position:absolute;right:14px;top:40px;font-size:7px;font-weight:600;color:var(--green);text-decoration:underline}
.stars{position:absolute;left:15px;top:72px;display:flex;gap:4px}
.reorder{position:absolute;right:14px;top:70px;font-size:10px;font-weight:600;display:flex;align-items:center;gap:2px}
.clip{position:absolute;left:0;top:120px;width:100%;height:406px;overflow:hidden}
</style>
</head>
<body>
<svg width="0" height="0" style="position:absolute">
  <defs>
    <symbol id="i-menu" viewBox="0 0 14 14"><circle cx="7" cy="7" r="7" fill="#e6e6e6"/><path d="M3.5 4.8h7M3.5 7h6M3.5 9.2h4" stroke="#222" stroke-width="1"/></symbol>
    <symbol id="i-qr" viewBox="0 0 14 14"><g fill="none" stroke="#222" stroke-width="1.6"><rect x="1" y="1" width="4.5" height="4.5"/><rect x="8.5" y="1" width="4.5" height="4.5"/><rect x="1" y="8.5" width="4.5" height="4.5"/></g><path d="M8.5 8.5h2v2h-2zM11 11h2v2h-2z" fill="#222"/></symbol>
    <symbol id="i-wallet" viewBox="0 0 16 14"><rect x="1" y="2" width="14" height="11" rx="2" fill="#222"/><rect x="10" y="6" width="5" height="3" fill="#fff"/></symbol>
    <symbol id="i-search" viewBox="0 0 12 12"><circle cx="5" cy="5" r="3.8" fill="none" stroke="#333" stroke-width="1.6"/><path d="M8 8l3 3" stroke="#333" stroke-width="1.6"/></symbol>
    <symbol id="i-pin" viewBox="0 0 8 11"><path d="M4 0.5a3.3 3.3 0 0 1 3.3 3.3C7.3 6.3 4 10.5 4 10.5S0.7 6.3 0.7 3.8A3.3 3.3 0 0 1 4 .5z" fill="#7bd13b"/><circle cx="4" cy="3.8" r="1.2" fill="#fff"/></symbol>
    <symbol id="i-star" viewBox="0 0 10 10"><path d="M5 .6l1.3 2.9 3.1.3-2.4 2 .8 3.1L5 7.3 2.2 8.9 3 5.8.6 3.8l3.1-.3z" fill="currentColor"/></symbol>
    <symbol id="i-redo" viewBox="0 0 10 10"><path d="M8.3 5A3.4 3.4 0 1 1 7.2 2.5" fill="none" stroke="#222" stroke-width="1.4"/><path d="M5.6 1.2h3v3z" fill="#222"/></symbol>
    <symbol id="i-home" viewBox="0 0 20 20"><path d="M3 9l7-6 7 6v8H3z" fill="none" stroke="#7bd13b" stroke-width="1.6" stroke-linejoin="round"/><path d="M8 17v-4h4v4" fill="none" stroke="#7bd13b" stroke-width="1.6"/></symbol>
    <symbol id="i-compass" viewBox="0 0 20 20"><circle cx="10" cy="10" r="8" fill="none" stroke="#333" stroke-width="1.5"/><path d="M13 7l-2 4-4 2 2-4z" fill="none" stroke="#333" stroke-width="1.4"/></symbol>
    <symbol id="i-list" viewBox="0 0 20 20"><circle cx="10" cy="10" r="8" fill="none" stroke="#333" stroke-width="1.5"/><path d="M6.5 7.5h7M6.5 10h7M6.5 12.5h5" stroke="#333" stroke-width="1.4"/></symbol>
    <symbol id="i-planet" viewBox="0 0 20 20"><circle cx="10" cy="10" r="6.5" fill="none" stroke="#333" stroke-width="1.5"/><path d="M3 13c-3 4 3 3 8 0s9-7 6-9" fill="none" stroke="#333" stroke-width="1.4"/></symbol>
    <symbol id="i-cup" viewBox="0 0 20 20"><path d="M4 8h11l-1.5 8h-8z" fill="none" stroke="#333" stroke-width="1.2"/><path d="M3 16.5h14" stroke="#333" stroke-width="1.2"/><path d="M7 6c0-2 2-2 2-4M10 6c0-2 2-2 2-4" fill="none" stroke="#333" stroke-width="1"/></symbol>
    <symbol id="i-tall" viewBox="0 0 20 20"><path d="M5 5h10l-1.5 13h-7z" fill="none" stroke="#333" stroke-width="1.2"/><path d="M4.5 3h11v2h-11z" fill="none" stroke="#333" stroke-width="1.2"/><circle cx="10" cy="11" r="2" fill="none" stroke="#333" stroke-width="1"/></symbol>
    <symbol id="i-snack" viewBox="0 0 20 20"><path d="M3 12h14M4 15h12M3 12l2-6 10 2 2 4" fill="none" stroke="#333" stroke-width="1.2"/><path d="M9 4l6-2" stroke="#333" stroke-width="1.2"/></symbol>
  </defs>
</svg>

<!-- Home screen -->
<section class="phone phone--home">
  <div class="abs status">12:22</div>
  <div class="abs status-icons"><svg width="22" height="6"><rect x="0" y="3" width="2" height="3" fill="#222"/><rect x="3" y="1" width="2" height="5" fill="#222"/><circle cx="10" cy="4" r="2" fill="#999"/><rect x="14" y="1" width="8" height="5" rx="1" fill="none" stroke="#222"/><rect x="15" y="2" width="3" height="3" fill="#222"/></svg></div>
  <header class="abs appbar">
    <svg class="abs menu" width="14" height="14"><use href="#i-menu"/></svg>
    <span class="abs title">HOME</span>
    <div class="abs brandmark"><div class="dot"></div><div class="name">PIXU</div></div>
    <svg class="abs qr" width="13" height="13"><use href="#i-qr"/></svg>
    <svg class="abs wallet" width="15" height="13"><use href="#i-wallet"/></svg>
  </header>
  <div class="abs hero" role="img" aria-label="Three brown sugar milkshakes topped with whipped cream"></div>
  <div class="abs hero-title">BROWN SUGAR</div>
  <div class="abs hero-sub">SERIES</div>
  <h2 class="abs h2" style="left:19px;top:293px">DEALS</h2>
  <div class="abs deal deal--a" role="img" aria-label="Promotion banner with coconut and boba pearls"></div>
  <div class="abs deal deal--b" role="img" aria-label="Promotion banner with a coffee cup"></div>
  <h2 class="abs h2" style="left:19px;top:441px">FAVOURITES</h2>
  <div class="abs card" style="top:467px">
    <div class="thumb" role="img" aria-label="Store interior photo"></div>
    <div class="name">Demo 2 Perth</div>
    <div class="addr"><svg width="7" height="10"><use href="#i-pin"/></svg>123 A Street Somewhere Here</div>
    <div class="fav"><svg width="11" height="11" style="color:#fff"><use href="#i-star"/></svg></div>
  </div>
  <nav class="abs navbar">
    <span class="navdot"></span>
    <svg class="navicon" style="left:24px" width="20" height="20"><use href="#i-home"/></svg>
    <svg class="navicon" style="left:92px" width="20" height="20"><use href="#i-compass"/></svg>
    <svg class="navicon" style="left:160px" width="20" height="20"><use href="#i-list"/></svg>
    <svg class="navicon" style="left:229px" width="20" height="20"><use href="#i-planet"/></svg>
  </nav>
</section>

<!-- Shop screen -->
<section class="phone phone--shop">
  <div class="abs status">12:22</div>
  <div class="abs status-icons"><svg width="22" height="6"><rect x="0" y="3" width="2" height="3" fill="#222"/><rect x="3" y="1" width="2" height="5" fill="#222"/><circle cx="10" cy="4" r="2" fill="#999"/><rect x="14" y="1" width="8" height="5" rx="1" fill="none" stroke="#222"/><rect x="15" y="2" width="3" height="3" fill="#222"/></svg></div>
  <header class="abs appbar">
    <svg class="abs menu" width="14" height="14"><use href="#i-menu"/></svg>
    <span class="abs title">HOME</span>
    <div class="abs brandmark"><div class="dot"></div><div class="name">PIXU</div></div>
    <svg class="abs qr" width="13" height="13"><use href="#i-qr"/></svg>
    <svg class="abs wallet" width="15" height="13"><use href="#i-wallet"/></svg>
  </header>
  <div class="abs search">Search<svg width="11" height="11"><use href="#i-search"/></svg></div>
  <h2 class="abs h2" style="left:19px;top:130px">CATEGORIES</h2>
  <div class="abs cat active" style="left:21px"><svg width="20" height="20"><use href="#i-cup"/></svg>Tea</div>
  <div class="abs cat" style="left:89px"><svg width="20" height="20"><use href="#i-cup"/></svg>Bubble<br>Tea</div>
  <div class="abs cat" style="left:157px"><svg width="20" height="20"><use href="#i-tall"/></svg>Coffee</div>
  <div class="abs cat" style="left:225px"><svg width="20" height="20"><use href="#i-snack"/></svg>Snacks</div>
  <h2 class="abs h2" style="left:19px;top:236px">BRANDS</h2>
  <div class="abs brand" style="left:22px;background:#1a73b8"></div>
  <div class="abs brand" style="left:65px;background:#233a8a"></div>
  <div class="abs brand" style="left:108px;background:#86c33f"></div>
  <div class="abs brand" style="left:151px;background:#1d9a55"></div>
  <h2 class="abs h2" style="left:19px;top:327px">STORES NEAR YOU</h2>
  <div class="abs card" style="top:352px">
    <div class="thumb" role="img" aria-label="Store interior photo"></div>
    <div class="name">Demo 2 Perth</div>
    <div class="addr"><svg width="7" height="10"><use href="#i-pin"/></svg>123 A Street Somewhere Here</div>
    <div class="fav"><svg width="11" height="11" style="color:#fff"><use href="#i-star"/></svg></div>
  </div>
  <div class="abs card" style="top:423px">
    <div class="thumb" role="img" aria-label="Store front photo" style="background:radial-gradient(circle at 45% 40%,#8c9a8a,#2c342e)"></div>
    <div class="name">Demo 2 Perth</div>
    <div class="addr"><svg width="7" height="10"><use href="#i-pin"/></svg>123 A Street Somewhere Here</div>
    <div class="fav"><svg width="11" height="11" style="color:#fff"><use href="#i-star"/></svg></div>
  </div>
  <div class="abs card" style="top:494px;opacity:.3">
    <div class="thumb" role="img" aria-label="Store counter photo"></div>
    <div class="name">Demo 2 Perth</div>
    <div class="addr"><svg width="7" height="10"><use href="#i-pin"/></svg>123 A Street Somewhere Here</div>
    <div class="fav"><svg width="11" height="11" style="color:#fff"><use href="#i-star"/></svg></div>
  </div>
  <nav class="abs navbar">
    <span class="navdot"></span>
    <svg class="navicon" style="left:24px" width="20" height="20"><use href="#i-home"/></svg>
    <svg class="navicon" style="left:92px" width="20" height="20"><use href="#i-compass"/></svg>
    <svg class="navicon" style="left:160px" width="20" height="20"><use href="#i-list"/></svg>
    <svg class="navicon" style="left:229px" width="20" height="20"><use href="#i-planet"/></svg>
  </nav>
</section>

<!-- Order history screen -->
<section class="phone phone--orders">
  <div class="abs status">12:22</div>
  <div class="abs status-icons"><svg width="22" height="6"><rect x="0" y="3" width="2" height="3" fill="#222"/><rect x="3" y="1" width="2" height="5" fill="#222"/><circle cx="10" cy="4" r="2" fill="#999"/><rect x="14" y="1" width="8" height="5" rx="1" fill="none" stroke="#222"/><rect x="15" y="2" width="3" height="3" fill="#222"/></svg></div>
  <header class="abs appbar">
    <svg class="abs menu" width="14" height="14"><use href="#i-menu"/></svg>
    <span class="abs title">HOME</span>
    <div class="abs brandmark"><div class="dot"></div><div class="name">PIXU</div></div>
    <svg class="abs qr" width="13" height="13"><use href="#i-qr"/></svg>
    <svg class="abs wallet" width="15" height="13"><use href="#i-wallet"/></svg>
  </header>
  <div class="abs search">Search<svg width="11" height="11"><use href="#i-search"/></svg></div>
  <div class="clip">
    <article class="abs order" style="top:11px">
      <div class="top"></div>
      <div class="thumb" role="img" aria-label="Store photo"></div>
      <div class="name">Demo 2 Perth</div>
      <div class="addr"><svg width="7" height="10"><use href="#i-pin"/></svg>123 a Street<br>Somewhere Here</div>
      <span class="badge">Delivered</span><span class="viewmenu">View Menu</span>
      <div class="stars" style="color:var(--star)"><svg width="9" height="9"><use href="#i-star"/></svg><svg width="9" height="9"><use href="#i-star"/></svg><svg width="9" height="9"><use href="#i-star"/></svg><svg width="9" height="9"><use href="#i-star"/></svg><svg width="9" height="9"><use href="#i-star"/></svg></div>
      <div class="reorder"><svg width="9" height="9"><use href="#i-redo"/></svg>Reorder</div>
    </article>
    <article class="abs order" style="top:117px">
      <div class="top"></div>
      <div class="thumb" role="img" aria-label="Store photo"></div>
      <div class="name">Demo 2 Perth</div>
      <div class="addr"><svg width="7" height="10"><use href="#i-pin"/></svg>123 a Street<br>Somewhere Here</div>
      <span class="badge">Delivered</span><span class="viewmenu">View Menu</span>
      <div class="stars" style="color:var(--star)"><svg width="9" height="9"><use href="#i-star"/></svg><svg width="9" height="9"><use href="#i-star"/></svg><svg width="9" height="9"><use href="#i-star"/></svg><svg width="9" height="9"><use href="#i-star"/></svg><svg width="9" height="9"><use href="#i-star"/></svg></div>
      <div class="reorder"><svg width="9" height="9"><use href="#i-redo"/></svg>Reorder</div>
    </article>
    <article class="abs order" style="top:223px">
      <div class="top"></div>
      <div class="thumb" role="img" aria-label="Store photo"></div>
      <div class="name">Demo 2 Perth</div>
      <div class="addr"><svg width="7" height="10"><use href="#i-pin"/></svg>123 a Street<br>Somewhere Here</div>
      <span class="badge">Delivered</span><span class="viewmenu">View Menu</span>
      <div class="stars" style="color:var(--star)"><svg width="9" height="9"><use href="#i-star"/></svg><svg width="9" height="9"><use href="#i-star"/></svg><svg width="9" height="9"><use href="#i-star"/></svg><svg width="9" height="9"><use href="#i-star"/></svg><svg width="9" height="9"><use href="#i-star"/></svg></div>
      <div class="reorder"><svg width="9" height="9"><use href="#i-redo"/></svg>Reorder</div>
    </article>
    <article class="abs order" style="top:329px">
      <div class="top"></div>
      <div class="thumb" role="img" aria-label="Store photo" style="background:radial-gradient(circle at 45% 40%,#8c9a9a,#2c3438)"></div>
      <div class="name">Demo 2 Perth</div>
      <div class="addr"><svg width="7" height="10"><use href="#i-pin"/></svg>123 a Street<br>Somewhere Here</div>
      <span class="badge">Delivered</span><span class="viewmenu">View Menu</span>
      <div class="stars" style="color:var(--star)"><svg width="9" height="9"><use href="#i-star"/></svg><svg width="9" height="9"><use href="#i-star"/></svg><svg width="9" height="9"><use href="#i-star"/></svg><svg width="9" height="9"><use href="#i-star"/></svg><svg width="9" height="9"><use href="#i-star"/></svg></div>
      <div class="reorder"><svg width="9" height="9"><use href="#i-redo"/></svg>Reorder</div>
    </article>
  </div>
  <nav class="abs navbar">
    <span class="navdot"></span>
    <svg class="navicon" style="left:24px" width="20" height="20"><use href="#i-home"/></svg>
    <svg class="navicon" style="left:92px" width="20" height="20"><use href="#i-compass"/></svg>
    <svg class="navicon" style="left:160px" width="20" height="20"><use href="#i-list"/></svg>
    <svg class="navicon" style="left:229px" width="20" height="20"><use href="#i-planet"/></svg>
  </nav>
</section>
</body>
</html>
```